Create an art-deco/vintage poster for restaurant

We need a poster to promote our new 'high tea' offering - Marlowe presents Miss Whitcombe's Splendid Old Fashioned Tea Parlour.
The poster will sit inside a chrome frame of an old art deco movie theatre. We'd like the poster to have an art-deco, vintage feel, while still looking fresh and eye catching to passers by. The size should be total 128cm tall by 72 cm wide. There's also a chrome band that sits 11-15cm down the poster that will be covered (see photo).
Wording should include along the lines of:
Indulge in a selection of savouries and sweets, decadent desserts, fine teas, coffee or bubbles with art-deco charm and fabulous views.
Served weekends from midday.

We'd also like a matching A4 menu border template.

Our logo, frame and inspiration images attached.

About the restaurant.
Set in the historic Regent picture theatre building, MARLOWE Restaurant and Bar at Katoomba combines playful art-deco charm with hearty food, friendly service and spectacular Blue Mountains views.
Located on main street Katoomba, enter the historic 1936 Regent picture theatre foyer and make your way past the ticket booth and up the stairs. The restaurant inhabits the dress circle of the old theatre, and offers a decor of quirky retro finds and spectacular mountain views over Leura and the Jamison Valley.

Meals are prepared in the old projection room, and cocktails and retro tunes are served in the former refreshment lounge, now a cosy bar complete with roaring fireplace. The art deco architecture is complemented by an eclectic collection of furnishings and artwork. The style of service is casual and friendly.

www.marlowedining.example.au

Target Market(s)

Tourists visiting the area, and locals who'd like to experience our new offering.

Industry/Entity Type

Restaurant

Font styles to use
Serif
Decorative
Script

Requirements
Must have
• Must be eye-catching to passers by, and suit the art deco style of the building. To be able to be printed and used in frame.
Nice to have
• Colourful.

```html
<!DOCTYPE html>
<html lang="en">
<head>
<meta charset="utf-8">
<title>Marlowe High Tea Poster</title>
<link rel="stylesheet" href="https://fonts.googleapis.com/css2?family=Federo&display=swap">
<style>
  :root {
    --stripe-red: #b5252b;
    --stripe-cream: #efe6d2;
    --gold: #c9a24a;
    --paper: #f3ede0;
    --paper-shade: #e8dfcb;
    --ink: #2b2523;
    --sign-dark: #1f1b1a;
    --sign-light: #ece4d2;
  }
  html, body {
    margin: 0;
    padding: 0;
    overflow: hidden;
    background: #ffffff;
  }
  .poster {
    position: relative;
    width: 675px;
    height: 1200px;
    overflow: hidden;
    background:
      repeating-linear-gradient(90deg,
        var(--stripe-cream) 0 6px,
        var(--gold) 6px 8px,
        var(--stripe-red) 8px 38px,
        var(--gold) 38px 40px,
        var(--stripe-cream) 40px 60px);
  }
  .brand-sign {
    position: absolute;
    left: 124px;
    top: 96px;
    width: 416px;
    height: 120px;
    box-sizing: border-box;
    background: var(--sign-light);
    border: 12px solid var(--sign-dark);
    outline: 3px solid var(--sign-light);
    outline-offset: -8px;
    display: flex;
    align-items: center;
    justify-content: center;
  }
  .brand-name {
    font-family: "Federo", sans-serif;
    font-size: 66px;
    line-height: 1;
    letter-spacing: 6px;
    color: var(--sign-dark);
  }
  .paper {
    position: absolute;
    left: 50px;
    top: 262px;
    width: 575px;
    height: 796px;
    background: linear-gradient(180deg, var(--paper) 0%, var(--paper-shade) 100%);
  }
  .floral-emblem {
    position: absolute;
    left: 180px;
    top: 340px;
    width: 315px;
    height: 232px;
    border-radius: 45%;
    background: radial-gradient(ellipse at center, #b9cfbd 0%, rgba(243,237,224,0) 70%);
  }
  .copy {
    position: absolute;
    left: 50px;
    width: 575px;
    margin: 0;
    text-align: center;
    color: var(--ink);
    font-family: "Federo", sans-serif;
    font-weight: 400;
  }
  .headline {
    top: 600px;
    font-size: 28px;
    line-height: 35px;
  }
  .divider {
    position: absolute;
    left: 322px;
    width: 30px;
    height: 2px;
    background: var(--ink);
  }
  .divider::before,
  .divider::after {
    content: "";
    position: absolute;
    top: -3px;
    width: 8px;
    height: 8px;
    border-radius: 50%;
    background: var(--ink);
  }
  .divider::before { left: -8px; }
  .divider::after { right: -8px; }
  .divider--one { top: 738px; }
  .divider--two { top: 956px; }
  .divider--three { top: 1042px; }
  .description {
    top: 768px;
    font-size: 22px;
    line-height: 37px;
  }
  .serving {
    top: 982px;
    font-size: 22px;
    line-height: 30px;
  }
  .flapper-illustration {
    position: absolute;
    left: 0;
    top: 890px;
    width: 124px;
    height: 310px;
    border-radius: 60px 60px 0 0;
    background: linear-gradient(170deg, #4f7d5e 0%, #c7a76b 45%, #b03a2e 100%);
  }
</style>
</head>
<body>
  <main class="poster">
    <section class="paper"></section>

    <div class="brand-sign">
      <span class="brand-name">MARLOWE</span>
    </div>

    <div class="floral-emblem" role="img" aria-label="Green art-deco floral emblem"></div>

    <h1 class="copy headline">MARLOWE presents:<br>Miss Whitcombe's Splendid<br>Old Fashioned Tea Parlour</h1>

    <div class="divider divider--one"></div>

    <p class="copy description">Indulge in a selection of savouries<br>and sweets, decadent desserts, fine teas,<br>coffee or bubbles with art-deco charm<br>and fabulous views.</p>

    <div class="divider divider--two"></div>

    <p class="copy serving">Served weekends from midday</p>

    <div class="divider divider--three"></div>

    <div class="flapper-illustration" role="img" aria-label="Illustration of a 1920s lady in a green cloche hat and red coat"></div>
  </main>
</body>
</html>
```